Web Design Project

I'm looking for a major redesign for my existing photographic art website: www.brightmeadowart.com. Here are my complaints about the current layout: 1) It looks unsophisticated (we will, of course, delete the "sale" banner; 2) the images are vastly too small when displayed in the gallery; 3) I'm not wild about the navigation; 4) the Flash has got to go; 4) there has to be an easy way to significantly enlarge the photos for viewing; 5) the copy is a bit over the top - we will be rewriting it. Other than that, it's a good site :)

The market for the photography is principally commercial applications - interior designers, etc. who are concerned with how these images will look in hospitals, office buildings, etc. The leading competitor in this space has a much better site: www.walterpriske.com. Another site worth viewing is: www.torvelt.com. This site is much more akin to my site.

We will be reducing the number of photos available. Total count will be approximately 400. The largest collection will be the "petal study" - close up photography of flowers, plants, etc.

I am amazed at the quality of the submissions - which has made the selection process very, very difficult. Each of you should be very proud of the quality of work you produce. Beyond this web-site, which is a "sideline" for me, I run a large marketing organization....and have shared these submissions with all of my colleagues who were duly impressed. Hopefully we will have an opportunity to work with you on a differentp project!

Thank you!!!
Mark

```html
<!DOCTYPE html>
<html lang="en">
<head>
<meta charset="utf-8">
<title>Bright Meadow — Photography by Mark Hollis</title>
<link rel="stylesheet" href="https://fonts.googleapis.com/css2?family=Arimo:wght@400;700&family=Noto+Serif:ital,wght@0,400;1,700&family=Open+Sans:wght@400;600&family=Poiret+One&display=swap">
<style>
:root{
  --bg-top:#1e1e1e;--bg-foot:#242424;--bg-base:#1a1a1a;--panel-dark:#2f2f2f;
  --white:#ffffff;--ink:#333333;--ink-soft:#555555;--grey-text:#8a8a8a;
  --red:#d80000;--red-dark:#a80000;--gold-top:#fcd46a;--gold-bot:#e0a21a;
  --sale:#e9e7a4;--blue:#1e8dc0;--panel-light:#ebebeb;--panel-line:#d6d6d6;
  --leaf-1:#5b8a2c;--leaf-2:#2f5a18;--wing:#c9772c;
}
*{box-sizing:border-box;margin:0;padding:0}
html,body{width:1105px;height:1200px;overflow:hidden}
body{position:relative;background:var(--white);font-family:Arimo,Arial,sans-serif;color:var(--ink)}
.abs{position:absolute}
.band-top{left:0;top:0;width:1105px;height:398px;background:var(--bg-top)}
.band-rule{left:0;width:1105px;height:4px;background:#cfcfcf}
.band-foot{left:0;top:846px;width:1105px;height:247px;background:var(--bg-foot)}
.band-base{left:0;top:1093px;width:1105px;height:107px;background:var(--bg-base)}

.brand-mark{width:57px;height:57px;background:#000;border:2px solid #fff}
.brand-name{font-weight:700;font-size:17px;color:var(--white);white-space:nowrap}
.tagline{font-family:"Noto Serif",Georgia,serif;font-style:italic;font-weight:700;font-size:12.5px;color:var(--white);white-space:nowrap}
.sale-title{font-family:"Poiret One",cursive;font-size:25px;color:var(--sale);white-space:nowrap;font-weight:400}
.sale-sub{font-family:"Poiret One",cursive;font-size:12px;color:var(--sale);white-space:nowrap}
.find-label{font-size:10.5px;color:var(--red);letter-spacing:.5px}
.find-input{left:700px;top:96px;width:97px;height:20px;background:#f2f2f2;border-radius:2px}
.btn-red{background:linear-gradient(#f01010,var(--red-dark));color:#fff;font-weight:700;font-size:10px;text-align:center;border-radius:3px}
.nav{left:390px;top:122px;width:500px;height:25px;background:linear-gradient(#3c3c3c,#0d0d0d);border-radius:3px;display:flex;align-items:center;padding-left:28px;font-family:"Open Sans",sans-serif;font-size:10px;color:#fff;white-space:nowrap}
.nav span.sep{margin:0 8px;color:#bbb}

.slider{left:207px;top:153px;width:692px;height:222px;background:#111;border-radius:6px}
.slide{top:161px;height:209px}
.slide-left{left:214px;width:339px;background:linear-gradient(160deg,#7c9a54 0%,var(--leaf-1) 35%,#3d4a2a 70%,#8a9a80 100%)}
.slide-right{left:555px;width:337px;background:radial-gradient(ellipse at 50% 45%,#2a3040 0%,#1e2530 20%,var(--leaf-1) 45%,var(--leaf-2) 100%)}
.slide-bar{left:214px;top:325px;width:678px;height:45px;background:rgba(20,20,20,.6)}
.dot{width:7px;height:7px;border-radius:50%;background:#7a7a7a;top:344px}
.slide-caption{left:671px;top:338px;width:139px;height:19px;background:linear-gradient(#fafafa,#d8d8d8);border-radius:2px;font-family:"Noto Serif",serif;font-style:italic;font-size:9px;color:#777;padding:4px 6px;letter-spacing:.5px}
.btn-gold{background:linear-gradient(var(--gold-top),var(--gold-bot));border-radius:3px;font-family:"Noto Serif",serif;font-size:9.5px;color:#3a2a00;text-align:center;box-shadow:0 1px 2px rgba(0,0,0,.25)}

.h-serif{font-family:"Noto Serif",Georgia,serif;font-weight:400;color:#333;white-space:nowrap}
.body-copy{font-size:9px;line-height:17.7px;color:var(--ink-soft)}
.photo{border:1px solid #bbb}
.photo-statue{left:207px;top:451px;width:156px;height:126px;background:linear-gradient(#a9b4c8 0%,#c7cdd8 55%,#3d4a32 75%,#7a8494 100%)}
.photo-artist{left:206px;top:592px;width:82px;height:95px;background:linear-gradient(#8c8c8c,#5a5a5a)}
.divider{left:288px;top:636px;width:352px;height:2px;background:linear-gradient(90deg,#d8d8d8,rgba(255,255,255,0))}

.side-box{background:var(--panel-light);border:1px solid var(--panel-line);border-radius:6px}
.btn-grey{background:linear-gradient(#a5b9b6,#6f8885);color:#111;font-family:"Noto Serif",serif;font-size:8px;border-radius:3px}
.thumb{top:682px;width:41px;height:51px}

.foot-head{font-family:"Noto Serif",Georgia,serif;font-size:16px;color:#ddd;white-space:nowrap}
.foot-box{top:907px;width:207px;height:156px;background:var(--panel-dark);border-radius:6px}
.foot-links{left:230px;top:919px;font-family:"Open Sans",sans-serif;font-size:10.5px;line-height:17.8px;color:#fff;list-style:none}
.foot-copy{font-size:8.8px;line-height:13.2px;color:var(--grey-text)}
.select{left:705px;top:1016px;width:97px;height:16px;background:#fff;border:1px solid #888;font-size:10px;color:#000;padding:1px 3px}
.base-links{left:207px;top:1106px;font-size:9px;color:#777;white-space:nowrap}
.social{top:1135px;width:22px;height:22px;border-radius:3px;background:#4d6a92}
</style>
</head>
<body>
<div class="abs band-top"></div>
<div class="abs band-rule" style="top:398px"></div>
<div class="abs band-rule" style="top:842px"></div>
<div class="abs band-foot"></div>
<div class="abs band-base"></div>

<!-- Header -->
<div class="abs brand-mark" style="left:251px;top:61px"></div>
<div class="abs brand-name" style="left:218px;top:123px">Bright Meadow</div>
<div class="abs tagline" style="left:343px;top:56px">Photography by Mark Hollis Photography</div>
<div class="abs tagline" style="left:396px;top:74px">that transcends our normal view of the world.</div>
<div class="abs sale-title" style="left:698px;top:44px">SALE 30% OFF</div>
<div class="abs sale-sub" style="left:698px;top:75px">ALL PHOTOGRAPHS</div>
<div class="abs find-label" style="left:627px;top:100px">Find a Photo</div>
<div class="abs find-input"></div>
<div class="abs btn-red" style="left:806px;top:96px;width:68px;height:21px;line-height:21px">search</div>
<nav class="abs nav">Gallery<span class="sep">|</span>Architects/Designers<span class="sep">|</span>About the Artist<span class="sep">|</span>Ordering Information<span class="sep">|</span>Contact Us</nav>

<!-- Slider -->
<div class="abs slider"></div>
<div class="abs slide slide-left" role="img" aria-label="Photograph of a monarch butterfly resting on a leaf"></div>
<div class="abs slide slide-right" role="img" aria-label="Photograph of a dark swallowtail butterfly among green leaves"></div>
<div class="abs slide-bar"></div>
<svg class="abs" style="left:226px;top:339px" width="36" height="16" viewBox="0 0 36 16">
  <path d="M1 8 L8 2 V5 H15 V11 H8 V14 Z" fill="#ddd"/>
  <path d="M35 8 L28 2 V5 H21 V11 H28 V14 Z" fill="#ddd"/>
</svg>
<div class="abs dot" style="left:271px;background:#aaa"></div>
<div class="abs dot" style="left:286px"></div>
<div class="abs dot" style="left:301px"></div>
<div class="abs dot" style="left:316px"></div>
<div class="abs dot" style="left:332px"></div>
<div class="abs slide-caption">BUTTERFLIES</div>
<div class="abs btn-gold" style="left:815px;top:338px;width:68px;height:19px;line-height:19px">view more..</div>

<!-- Intro -->
<h1 class="abs h-serif" style="left:208px;top:420px;font-size:18px">Photography by Mark Hollis</h1>
<div class="abs photo photo-statue" role="img" aria-label="Photograph of a horse and rider statue against a city skyline"></div>
<p class="abs body-copy" style="left:374px;top:460px;width:284px">Welcome to the world of Mark Hollis. Come in and enjoy a place where stunning horizons meet glorious skies. A place where light and shade dance together in flawless rhythm. Come in and discover a world of photography that begins and ends with a shutter. Come in, relax and browse the gallery. You are about to experience some of the most inspiring and enchanting imagery the world has to offer.</p>
<div class="abs btn-gold" style="left:587px;top:575px;width:68px;height:21px;line-height:21px">Learn more</div>

<!-- About the artist -->
<div class="abs photo photo-artist" role="img" aria-label="Portrait photograph of the artist"></div>
<div class="abs divider"></div>
<h2 class="abs h-serif" style="left:297px;top:657px;font-size:16px">About the Artist</h2>
<p class="abs body-copy" style="left:206px;top:690px;width:210px">It takes a special talent to create photography that captivates our interest, evokes our emotions and transcends our normal view of the world. This is the world of Mark Hollis.<br>As a young sports photographer for the Riverton Hawks baseball team, Mark Hollis found that preci-sion and timing were key.....</p>
<div class="abs btn-gold" style="left:338px;top:811px;width:68px;height:21px;line-height:21px">Learn more</div>

<!-- Architects -->
<svg class="abs" style="left:450px;top:660px" width="26" height="26" viewBox="0 0 26 26">
  <path d="M3 23 L23 23 L3 5 Z" fill="none" stroke="#777" stroke-width="1.5"/>
  <path d="M9 20 L21 3" stroke="#4a7bb8" stroke-width="3"/>
</svg>
<h2 class="abs h-serif" style="left:484px;top:662px;font-size:16px">Architects &amp; Designers</h2>
<p class="abs body-copy" style="left:443px;top:690px;width:216px">A specialized division of our company is dedicated to exclusively serving architects, interior designers, art consultants and other professionals involved in the selection and procurement of commercial artwork. The company provides these professionals with access to Mark Hollis's broad collection of photographic artwork,</p>
<div class="abs btn-gold" style="left:582px;top:811px;width:69px;height:21px;line-height:21px">Learn more</div>

<!-- Sidebar -->
<h2 class="abs h-serif" style="left:700px;top:448px;font-size:16px">To Order</h2>
<div class="abs h-serif" style="left:790px;top:451px;font-size:13px;color:#555">Login &nbsp;|&nbsp; Sign Up</div>
<div class="abs side-box" style="left:690px;top:471px;width:209px;height:122px"></div>
<div class="abs" style="left:705px;top:480px;font-family:'Noto Serif',serif;font-size:9.5px;color:#666">You have 0 item(s) in your cart.</div>
<div class="abs btn-red" style="left:707px;top:511px;width:69px;height:22px;line-height:22px;font-family:'Noto Serif',serif;font-weight:400;font-size:8px;color:#111">LIGHT BOX</div>
<div class="abs btn-grey" style="left:800px;top:511px;width:69px;height:22px;padding:6px 0 0 14px">CART</div>
<svg class="abs" style="left:843px;top:515px" width="18" height="14" viewBox="0 0 18 14">
  <path d="M1 2 H17 L15 13 H3 Z" fill="#d00"/>
  <path d="M6 4 V11 M9 4 V11 M12 4 V11" stroke="#fff" stroke-width="1"/>
</svg>
<h2 class="abs h-serif" style="left:706px;top:611px;font-size:15px">SALE</h2>
<div class="abs side-box" style="left:690px;top:641px;width:209px;height:158px"></div>
<div class="abs" style="left:706px;top:656px;font-size:10.5px;font-weight:700;color:var(--blue)">Photography by Mark Hollis</div>
<div class="abs thumb" style="left:703px;background:linear-gradient(#2a3a55,#0e1420)" role="img" aria-label="Thumbnail of office towers at dusk"></div>
<div class="abs thumb" style="left:753px;background:radial-gradient(#c86a2a,#1a0e08)" role="img" aria-label="Thumbnail of a city street at night"></div>
<div class="abs thumb" style="left:802px;background:linear-gradient(#3b7ac8,#c9a86a)" role="img" aria-label="Thumbnail of a sunlit building facade"></div>
<div class="abs thumb" style="left:851px;background:linear-gradient(#c8ccd2,#2e3236)" role="img" aria-label="Thumbnail of a skyscraper seen from below"></div>
<p class="abs foot-copy" style="left:703px;top:742px;width:195px;color:#666;line-height:16.5px">SALE! All photographs 30% off.<br>Discount will be applied automatically in the shopping cart as part of the ordering process.</p>

<!-- Footer -->
<svg class="abs" style="left:207px;top:870px" width="22" height="22" viewBox="0 0 24 24">
  <path d="M12 1 L15 8.5 L23 9 L17 14.5 L19 22.5 L12 18 L5 22.5 L7 14.5 L1 9 L9 8.5 Z" fill="#f5b82a"/>
</svg>
<h3 class="abs foot-head" style="left:237px;top:872px">Links</h3>
<h3 class="abs foot-head" style="left:482px;top:872px">About the Artist</h3>
<h3 class="abs foot-head" style="left:720px;top:872px">Gallery</h3>
<div class="abs foot-box" style="left:207px"></div>
<div class="abs foot-box" style="left:452px"></div>
<div class="abs foot-box" style="left:690px"></div>
<ul class="abs foot-links">
  <li>Gallery</li><li>Architects/Designers</li><li>About the Artist</li><li>Ordering Information</li><li>Contact Us</li>
</ul>
<div class="abs" style="left:465px;top:913px;width:68px;height:78px;border:1px solid #ccc;background:linear-gradient(#9a9a9a,#5e5e5e)" role="img" aria-label="Portrait photograph of the artist"></div>
<p class="abs foot-copy" style="left:465px;top:993px;width:185px">It takes a special talent to create photogra-phy that captivates our interest, evokes our emotions and transcends our normal view of the world. This is the world of Mark Hollis.</p>
<p class="abs foot-copy" style="left:701px;top:918px;width:185px">Please select a Category from the menu below. Some categories have sub-categories as well to help you narrow down your search. Click on the thumbnail to view a larger image along with frame and mat choices.</p>
<div class="abs" style="left:705px;top:993px;font-size:9px;color:var(--red)">CATEGORIES</div>
<div class="abs select">Butterflies</div>
<svg class="abs" style="left:789px;top:1018px" width="11" height="12" viewBox="0 0 11 12">
  <rect width="11" height="12" fill="#ddd" stroke="#888"/><path d="M2.5 4 H8.5 L5.5 8 Z" fill="#000"/>
</svg>

<!-- Base -->
<div class="abs base-links">Gallery | Architects/Designers | About the Artist | Ordering Information | Contact Us</div>
<div class="abs" style="left:582px;top:1105px;font-size:11px;color:#fff">Phone: 555-014-2236</div>
<div class="abs" style="left:730px;top:1106px;font-size:9px;color:#777">© 2010 Hollis Photography</div>
<div class="abs brand-mark" style="left:220px;top:1128px;width:40px;height:40px"></div>
<div class="abs brand-name" style="left:277px;top:1133px;font-size:13px">Bright Meadow</div>
<div class="abs" style="left:548px;top:1139px;font-size:7px;color:#555">Follow us on social network</div>
<div class="abs social" style="left:665px"></div>
<div class="abs social" style="left:697px"></div>
<div class="abs social" style="left:729px"></div>
<div class="abs social" style="left:761px"></div>
<div class="abs social" style="left:793px"></div>
<div class="abs social" style="left:824px"></div>
</body>
</html>
```